Card Design for my dog training business Rustpaw Obedience

Need a business card design for my dog training business with my new logo. Want the card to come off professional yet fun. Want it to be very eye catchy as well. I normally have these at vet clinics, pet stores, and groomers. so need it to look better than my competitors.
Target Market(s)
dog owners
Industry/Entity Type
Dog Training
Contact Information for Business Card
needs logo, my name and info
Font styles to use
Serif
Colors
0255a3
ffffff
ec1f27
000000
333333
fbfbfb
Requirements
Must have
- Rustpaw Obedience
- Hollis Brandt
- 415 903 2267
- info@rustpawobedience.example
- www.rustpawobedience.example

```html
<!DOCTYPE html>
<html lang="en">
<head>
<meta charset="utf-8">
<title>Rustpaw Obedience – Business Card</title>
<link rel="stylesheet" href="https://fonts.googleapis.com/css2?family=Tinos:wght@400;700&family=Open+Sans:wght@400;600&display=swap">
<style>
  :root {
    --stage: #f0f0f2;
    --card-dark: #333333;
    --card-light: #ffffff;
    --ink: #333333;
    --ink-soft: #7a7a7a;
    --title-grey: #d8d8d8;
    --white: #ffffff;
    --shadow: rgba(0, 0, 0, 0.28);
  }
  * { box-sizing: border-box; margin: 0; padding: 0; }
  html, body {
    width: 1200px;
    height: 1200px;
    overflow: hidden;
    background: var(--stage);
  }
  .canvas {
    position: relative;
    width: 1200px;
    height: 1200px;
  }
  .card {
    position: absolute;
    left: 254px;
    width: 723px;
    height: 413px;
    border-radius: 18px;
    overflow: hidden;
    box-shadow: 2px 4px 7px var(--shadow);
  }

  /* Front */
  .card--front {
    top: 186px;
    background: var(--card-dark);
  }
  .front-brand {
    position: absolute;
    left: 0;
    right: 0;
    top: 150px;
    text-align: center;
    font-family: "Tinos", serif;
    font-weight: 400;
    color: var(--white);
    font-size: 46px;
    line-height: 1.1;
    letter-spacing: 4px;
  }
  .front-tagline {
    position: absolute;
    left: 0;
    right: 0;
    top: 313px;
    text-align: center;
    font-family: "Open Sans", sans-serif;
    font-size: 13px;
    color: var(--white);
  }

  /* Back */
  .card--back {
    top: 644px;
    background: var(--card-light);
  }
  .back-band {
    position: absolute;
    left: 0;
    top: 0;
    width: 723px;
    height: 170px;
  }
  .back-title {
    position: absolute;
    left: 41px;
    top: 58px;
    font-family: "Tinos", serif;
    font-size: 31px;
    letter-spacing: 0.5px;
    color: var(--title-grey);
    text-transform: uppercase;
  }
  .back-brand {
    position: absolute;
    left: 470px;
    width: 230px;
    top: 190px;
    text-align: center;
    font-family: "Tinos", serif;
    font-weight: 400;
    color: var(--ink);
    font-size: 32px;
    line-height: 1.1;
    letter-spacing: 3px;
  }
  .holder-name {
    position: absolute;
    left: 41px;
    top: 260px;
    font-family: "Tinos", serif;
    font-size: 24px;
    text-transform: uppercase;
    color: var(--ink);
  }
  .holder-name .first { font-weight: 700; }
  .holder-name .last { font-weight: 400; color: var(--ink-soft); }
  .name-rule {
    position: absolute;
    left: 41px;
    top: 304px;
    width: 448px;
    height: 3px;
    background: var(--ink);
  }
  .contact-list {
    position: absolute;
    left: 41px;
    top: 316px;
    list-style: none;
    font-family: "Open Sans", sans-serif;
    font-size: 15px;
    color: var(--ink);
  }
  .contact-list li {
    display: flex;
    align-items: center;
    height: 21px;
  }
  .contact-icon {
    width: 14px;
    height: 14px;
    margin-right: 12px;
    flex: none;
  }
</style>
</head>
<body>
<main class="canvas">

  <section class="card card--front" aria-label="Card front">
    <div class="front-brand">RUSTPAW<br>OBEDIENCE</div>
    <p class="front-tagline">“Training dogs across Texas one dog at a time.”</p>
  </section>

  <section class="card card--back" aria-label="Card back">
    <svg class="back-band" viewBox="0 0 723 170" aria-hidden="true">
      <path fill="var(--card-dark)" d="M0 0 H723 V150 L706 147 L690 152 L672 146 L655 150 L640 144 L622 149 L604 143 L590 148 L572 142 L556 146 L540 140 L522 145 L505 139 L488 143 L470 136 L452 140 L436 134 L418 139 L400 133 L382 137 L364 131 L346 136 L330 130 L312 134 L294 128 L276 133 L258 127 L240 132 L222 126 L206 131 L188 125 L170 130 L152 124 L134 129 L116 123 L98 128 L80 122 L62 127 L44 121 L26 126 L10 120 L0 124 Z"/>
    </svg>
    <h1 class="back-title">Rustpaw Obedience</h1>
    <div class="back-brand">RUSTPAW<br>OBEDIENCE</div>

    <p class="holder-name"><span class="first">Hollis</span> <span class="last">Brandt</span></p>
    <div class="name-rule"></div>

    <ul class="contact-list">
      <li>
        <svg class="contact-icon" viewBox="0 0 14 14" aria-hidden="true">
          <rect width="14" height="14" rx="2" fill="var(--ink)"/>
          <path fill="var(--white)" d="M4 3 L5.6 3 L6.3 5 L5.3 5.8 Q6.3 7.8 8.2 8.7 L9 7.7 L11 8.4 L11 10 Q10.5 11 9.5 11 Q6 10.5 3.5 7 Q3 5.5 3 4 Q3 3 4 3 Z"/>
        </svg>
        415 903 2267
      </li>
      <li>
        <svg class="contact-icon" viewBox="0 0 14 14" aria-hidden="true">
          <rect width="14" height="14" rx="2" fill="var(--ink)"/>
          <rect x="3" y="4" width="8" height="6" fill="none" stroke="var(--white)" stroke-width="1"/>
          <path d="M3 4 L7 7.5 L11 4" fill="none" stroke="var(--white)" stroke-width="1"/>
        </svg>
        info@rustpawobedience.example
      </li>
      <li>
        <svg class="contact-icon" viewBox="0 0 14 14" aria-hidden="true">
          <rect width="14" height="14" rx="2" fill="var(--ink)"/>
          <circle cx="7" cy="7" r="4" fill="none" stroke="var(--white)" stroke-width="1"/>
          <ellipse cx="7" cy="7" rx="1.7" ry="4" fill="none" stroke="var(--white)" stroke-width="0.9"/>
          <path d="M3 7 H11" stroke="var(--white)" stroke-width="0.9"/>
        </svg>
        www.rustpawobedience.example
      </li>
    </ul>
  </section>

</main>
</body>
</html>
```